Medical Skincare services/menu/pricing Booklet 12 pages

We need produce a 12-page glossy, saddle-stitched booklet (5 1/2" tall X 81/2" wide). The booklet will be used as a services menu for a skin care salon. I have mocked up the booklet (w/ all copy) in WORD and I've provided a separate PDF of the accurate page order (see files attached). IMPORTANT: Feel free to use your creativity yet style-wise it should kinda match my wife's website colors and text style. Her clients are demanding so she wants a clean, high end, modern look (ala Apple maybe?). See her website for a frame of reference www.GlowWithMira.com

Target Market(s)

upscale female, professional women, teens with acne

Industry/Entity Type

Medical

Requirements
Must have
• the pics in the mock up are important. I've attached them here

```html
<!DOCTYPE html>
<html lang="en">
<head>
<meta charset="utf-8">
<title>Glow with Mira – Services Booklet Covers</title>
<link href="https://fonts.googleapis.com/css2?family=Open+Sans:ital,wght@0,300;0,400;0,700;0,800;1,300;1,400&display=swap" rel="stylesheet">
<style>
  :root {
    --backdrop: #9c9c9c;
    --ink: #050505;
    --paper: #ffffff;
    --studio: #f1f1f1;
    --silver: #d9d9d9;
    --text-light: #f4f4f4;
    --text-muted: #cfcfcf;
    --icon-dot: #8a8a8a;
  }
  * { box-sizing: border-box; margin: 0; padding: 0; }
  html, body { width: 1200px; height: 900px; overflow: hidden; }
  body {
    background: var(--backdrop);
    font-family: "Open Sans", Arial, sans-serif;
    position: relative;
  }
  .spread {
    position: absolute;
    left: 50px; top: 272px;
    width: 1100px; height: 356px;
    display: flex;
    box-shadow: 0 10px 30px rgba(0,0,0,.25);
  }
  .page { position: relative; width: 550px; height: 356px; overflow: hidden; }

  /* Back cover */
  .back-cover { background: var(--paper); }
  .portrait {
    position: absolute; left: 0; top: 0; width: 238px; height: 290px;
    background: linear-gradient(180deg, var(--studio), #e2e2e2);
  }
  .portrait-photo {
    position: absolute; left: 40px; top: 18px; width: 170px; height: 272px;
    background: radial-gradient(ellipse at 50% 35%, #8b7560 0%, #6d6d6d 35%, #4a4a4a 70%, #e6e6e6 100%);
    border-radius: 40% 40% 6px 6px;
  }
  .owner-band {
    position: absolute; left: 0; top: 226px; width: 238px; height: 56px;
    background: var(--ink); color: var(--text-light);
    padding: 10px 0 0 46px;
  }
  .owner-name { font-weight: 300; font-size: 11px; letter-spacing: .3px; }
  .owner-title { font-weight: 400; font-size: 10px; margin-top: 2px; }
  .contact-panel {
    position: absolute; left: 238px; top: 0; width: 312px; height: 356px;
    background: var(--ink); color: var(--text-light);
  }
  .contact-foot {
    position: absolute; left: 238px; bottom: 0; width: 312px; height: 40px;
    background: var(--ink);
  }
  .book-online {
    position: absolute; right: 36px; top: 38px;
    font-weight: 800; font-style: italic; font-size: 15px;
  }
  .site-link {
    position: absolute; right: 36px; top: 62px;
    font-size: 14px; font-weight: 300; display: flex; align-items: center; gap: 7px;
  }
  .site-link b { font-weight: 700; }
  .hours {
    position: absolute; right: 56px; top: 104px;
    font-size: 8.5px; font-style: italic; font-weight: 300;
    text-align: right; line-height: 12px; color: var(--text-muted);
  }
  .address {
    position: absolute; right: 60px; top: 205px;
    font-size: 9px; font-style: italic; font-weight: 300;
    text-align: right; line-height: 12.5px;
  }
  .address .studio-name { font-weight: 400; }
  .phone, .email {
    position: absolute; right: 60px;
    font-size: 9px; font-style: italic; font-weight: 300;
    display: flex; align-items: center; gap: 5px;
  }
  .phone { top: 262px; }
  .email { top: 280px; }
  .divider {
    position: absolute; left: 238px; bottom: 36px; width: 180px; height: 1px;
    background: linear-gradient(90deg, transparent, var(--silver));
  }
  .social-dots { position: absolute; right: 112px; bottom: 14px; display: flex; gap: 6px; }
  .social-dots span { width: 12px; height: 12px; border-radius: 50%; background: var(--icon-dot); }

  /* Front cover */
  .front-cover {
    background: linear-gradient(100deg, #1a1a1a 0%, #3b3b3b 6%, #0d0d0d 22%, #050505 60%, #121212 100%);
  }
  .wordmark {
    position: absolute; left: 100px; top: 110px; width: 420px;
    color: var(--silver); font-weight: 800; text-transform: uppercase;
    font-size: 56px; line-height: 58px; letter-spacing: 1px;
  }
  .wordmark small { display: block; font-size: 22px; line-height: 28px; letter-spacing: 6px; }
  .cover-url {
    position: absolute; left: 96px; top: 288px;
    color: var(--text-light); font-size: 15px; font-weight: 300;
  }
  .cover-url b { font-weight: 700; }
  .cover-rule {
    position: absolute; left: 0; top: 316px; width: 190px; height: 2px;
    background: linear-gradient(90deg, #bfbfbf, var(--paper));
  }
</style>
</head>
<body>
  <div class="spread">
    <section class="page back-cover">
      <div class="portrait">
        <div class="portrait-photo" role="img" aria-label="Portrait of the owner, a woman with long brown hair in a grey knit top and fur vest"></div>
      </div>
      <div class="contact-panel">
        <div class="book-online">BOOK ONLINE</div>
        <div class="site-link">
          <svg width="12" height="13" viewBox="0 0 12 13" aria-hidden="true"><path d="M4 1v7M4 4h2v4M6 5h2v3M8 6h2v3c0 2-1 3-3 3H6C4 12 2 10 2 8V6h2" fill="none" stroke="#f4f4f4" stroke-width="1"/></svg>
          <span>www.<b>GlowWithMira</b>.com</span>
        </div>
        <div class="hours">
          Sunday: Closed<br>
          Monday: 10:00am–4:00pm<br>
          Tuesday: 10:00am–6:00pm<br>
          Wednesday: 10:00am–6:00pm<br>
          Thursday: 10:00am–6:00pm<br>
          Friday: 10:00am–4:00pm<br>
          Saturday: 10:00am–4:00pm
        </div>
        <div class="address">
          <span class="studio-name">Glow with Mira</span><br>
          <svg width="8" height="10" viewBox="0 0 8 10" aria-hidden="true"><path d="M4 9.5C1.5 6 1 5 1 4a3 3 0 0 1 6 0c0 1-.5 2-3 5.5z" fill="none" stroke="#f4f4f4" stroke-width="1"/><circle cx="4" cy="4" r="1" fill="#f4f4f4"/></svg>
          4120 Aspen Ridge Rd #210<br>
          Cedar Hollow, CO 80999
        </div>
        <div class="phone">
          <svg width="9" height="9" viewBox="0 0 10 10" aria-hidden="true"><circle cx="5" cy="5" r="4.3" fill="none" stroke="#f4f4f4" stroke-width="1"/><path d="M3.4 3c.3 1.8 1.6 3.3 3.4 3.8l.4-.8-1-.5-.5.4C5 5.4 4.6 5 4.3 4.4l.4-.5-.5-1z" fill="#f4f4f4"/></svg>
          555-014-2287
        </div>
        <div class="email">
          <svg width="10" height="8" viewBox="0 0 10 8" aria-hidden="true"><rect x=".5" y=".5" width="9" height="7" fill="none" stroke="#f4f4f4"/><path d="M.5.5 5 4.5 9.5.5" fill="none" stroke="#f4f4f4"/></svg>
          mira@glowwithmira.com
        </div>
      </div>
      <div class="owner-band">
        <div class="owner-name">MIRA HALDEN</div>
        <div class="owner-title">(MEDICAL AESTHETICIAN &amp; OWNER)</div>
      </div>
      <div class="divider"></div>
      <div class="social-dots" aria-hidden="true"><span></span><span></span><span></span><span></span></div>
    </section>

    <section class="page front-cover">
      <div class="wordmark">Glow<small>with</small>Mira</div>
      <div class="cover-url">www.<b>GlowWithMira</b>.com</div>
      <div class="cover-rule"></div>
    </section>
  </div>
</body>
</html>
```